Pamphlet for IT Services Company (MSP Provider or Managed Services Provider)

We need a pamphlet designed for our Managed Services Company. We are an established company of 17 years that has never advertised. We'd like a pamphlet that we can drop off at potential client sites that describes our services. I like clean and prefer Orange as an accent color. We'd like to touch on the fact that we cater to our clients needs and go above and beyond what the other providers do.

Target Market(s)

Small and Medium Sized Businesses

Industry/Entity Type

It Service

Font styles to use
Other font styles liked:
• Try to match font on logo or website

Requirements
Must have
• Must highlight with the following Services and descriptions with Logo
Managed IT Services
IT Support
VOIP Solutions
WiFI Solutions
Contact information with phone number and website address.
Please view website korvantech.com
try to match fons on website above.
Nice to have
• Customer Testimonials. May a couple one line testimonials. Not real sure because this is the first time we've ever designed a brochure.
Should not have
• Not Sure

```html
<!DOCTYPE html>
<html lang="en">
<head>
<meta charset="utf-8">
<title>Korvan Technologies – Managed IT Services</title>
<link href="https://fonts.googleapis.com/css2?family=Dosis:wght@500;600&family=Noto+Sans:wght@400;600&display=swap" rel="stylesheet">
<style>
  :root{
    --orange:#ee7623;
    --orange-light:#f3a362;
    --navy:#212a36;
    --ink:#1e2530;
    --white:#ffffff;
    --badge:#e6e6e6;
    --badge-dark:#555555;
  }
  *{margin:0;padding:0;box-sizing:border-box}
  html,body{width:949px;height:1200px;overflow:hidden;background:var(--white)}
  .flyer{position:relative;width:949px;height:1200px;background:var(--white);font-family:"Noto Sans",sans-serif;color:var(--ink)}
  .service{position:absolute;bottom:229px;width:215.5px;color:var(--white);padding-left:13px}
  .service--orange{background:var(--orange)}
  .service--navy{background:var(--navy)}
  .service__icon{position:absolute;top:0;left:13px;width:72px;height:72px}
  .service__title{position:absolute;left:13px;font-weight:600;font-size:17.5px;line-height:1}
  .service__lead{font-weight:600;font-size:13.5px;margin-bottom:16px}
  .service__body{position:absolute;left:13px;right:6px;font-size:12.3px;line-height:15.3px}
  .hero{position:absolute;left:0;top:0;width:949px;height:660px}
  .brand{position:absolute;left:561px;top:38px;display:flex;align-items:center;gap:10px;color:var(--orange);font-family:"Dosis",sans-serif;font-weight:500;font-size:30px}
  .brand__dot{width:22px;height:22px;border-radius:50%;background:var(--orange)}
  .headline{position:absolute;left:500px;top:150px;font-family:"Dosis",sans-serif;font-weight:600;font-size:76px;line-height:90px;color:var(--ink)}
  .tagline{position:absolute;left:502px;top:336px;font-family:"Dosis",sans-serif;font-weight:600;font-size:30px;line-height:42px;color:var(--ink)}
  .quote{position:absolute;left:502px;top:452px;font-size:14.5px;color:var(--ink)}
  .contact{position:absolute;top:1012px;display:flex;align-items:center;gap:12px;font-weight:600;font-size:14.5px;line-height:19px}
  .contact__icon{width:26px;height:26px;border-radius:50%;background:var(--orange);display:flex;align-items:center;justify-content:center;flex:none}
  .partner{position:absolute;top:1104px;height:62px;background:var(--badge)}
  .partner--dark{background:var(--badge-dark);top:1110px;height:50px}
</style>
</head>
<body>
<main class="flyer">

  <section class="service service--orange" style="left:43px;top:480px">
    <svg class="service__icon" style="top:150px" viewBox="0 0 72 72" fill="none" stroke="#fff" stroke-width="3">
      <rect x="4" y="28" width="40" height="28" rx="2"/><path d="M0 60h52"/>
      <circle cx="48" cy="24" r="14"/><circle cx="48" cy="24" r="5"/>
      <path d="M48 4v6M48 38v6M28 24h6M62 24h6M34 10l4 4M58 34l4 4M62 10l-4 4M38 34l-4 4"/>
    </svg>
    <h2 class="service__title" style="top:256px">Managed IT Services</h2>
    <div class="service__body" style="top:282px">
      <p class="service__lead">Let us take care of your IT</p>
      <p>Our MSP is a Flat Rate service that includes Onsite Remote Support, Endpoint Protection, Web Filtering, Encrypted Online Backup &amp; Patch Management.</p>
    </div>
  </section>

  <section class="service service--navy" style="left:258.5px;top:590px">
    <svg class="service__icon" style="top:40px" viewBox="0 0 72 72" fill="#fff">
      <path d="M36 10l4 0 2 7 6 3 7-3 3 3-3 7 3 6 7 2v4l-7 2-3 6 3 7-3 3-7-3-6 3-2 7h-4l-2-7-6-3-7 3-3-3 3-7-3-6-7-2v-4l7-2 3-6-3-7 3-3 7 3 6-3z"/>
      <circle cx="38" cy="36" r="9" fill="var(--navy)"/>
    </svg>
    <h2 class="service__title" style="top:146px">IT Support</h2>
    <p class="service__body" style="top:172px">We have a passion for what we do and it shows! Korvan provides fast, reliable, expert solutions from experienced staff. You will never feel like just another client to us because our customers are family!</p>
  </section>

  <section class="service service--orange" style="left:474px;top:620px">
    <svg class="service__icon" style="top:22px" viewBox="0 0 72 72" fill="#fff">
      <path d="M14 8c4-2 8 0 10 4l5 9c1 3 0 5-2 7l-4 3c3 7 9 13 16 16l3-4c2-2 5-3 7-2l9 5c4 2 6 6 4 10l-3 5c-3 4-8 5-13 3C31 59 13 41 8 24c-2-5-1-10 3-13z"/>
      <path d="M40 12a20 20 0 0 1 20 20M40 4a28 28 0 0 1 28 28M40 20a12 12 0 0 1 12 12" fill="none" stroke="#fff" stroke-width="4"/>
    </svg>
    <h2 class="service__title" style="top:128px">VOIP Solutions</h2>
    <p class="service__body" style="top:154px">Phones are more than just an attachment to a desk. Allow us to help you maximize communication with your team and customers by using the latest technology that will likely save you money as well. Korvan Technologies partners with Relay to provide phone hardware, systems, and phone service.</p>
  </section>

  <section class="service service--navy" style="left:689.5px;top:612px">
    <svg class="service__icon" style="top:24px" viewBox="0 0 72 72" fill="none" stroke="#fff" stroke-width="3">
      <rect x="14" y="16" width="52" height="38" rx="2"/><rect x="19" y="21" width="42" height="28"/>
      <path d="M36 54v6M26 64h20l-3-4H29z"/>
      <circle cx="6" cy="12" r="2" fill="#fff"/><path d="M2 6a8 8 0 0 1 10 6M2 0a14 14 0 0 1 16 12"/>
    </svg>
    <h2 class="service__title" style="top:136px">WiFi Solutions</h2>
    <p class="service__body" style="top:162px">WiFi is everywhere! (At least it should be.) Korvan can extend your WiFi to cover your whole campus.</p>
  </section>

  <svg class="hero" viewBox="0 0 949 660">
    <defs>
      <radialGradient id="heroTone" cx="0.62" cy="0.3" r="0.8">
        <stop offset="0" stop-color="#fffaf2"/>
        <stop offset="0.35" stop-color="#f6dcc0"/>
        <stop offset="0.6" stop-color="#7d5a44"/>
        <stop offset="1" stop-color="#1a1716"/>
      </radialGradient>
    </defs>
    <path d="M0 475 Q470 740 949 475 L949 520 Q520 790 100 530 L0 480Z" fill="var(--orange)"/>
    <path d="M0 475 Q470 740 949 475 L949 492 Q480 760 0 478Z" fill="var(--orange-light)"/>
    <path d="M0 0H949V475Q470 740 0 475Z" fill="url(#heroTone)" role="img" aria-label="Photo of a businessman pointing at a glowing cloud with service icons"/>
  </svg>

  <div class="brand"><span class="brand__dot"></span>korvan technologies</div>
  <h1 class="headline">Managed<br>IT Services</h1>
  <p class="tagline">A Simple, Cost Effective Plan<br>for your IT Infrastructure.</p>
  <p class="quote">“Wouldn't it be nice if your stuff just worked?”</p>

  <div class="contact" style="left:68px">
    <span class="contact__icon"><svg width="14" height="16" viewBox="0 0 14 16"><path d="M7 0a6 6 0 0 1 6 6c0 4-6 10-6 10S1 10 1 6a6 6 0 0 1 6-6z" fill="var(--navy)"/><circle cx="7" cy="6" r="2" fill="var(--orange)"/></svg></span>
    <span>PO Box 412<br>Millbrook MO 63190 United States</span>
  </div>
  <div class="contact" style="left:447px">
    <span class="contact__icon"><svg width="14" height="14" viewBox="0 0 14 14"><path d="M2 1c1-1 2 0 3 1l1 2c0 1 0 1-1 2 1 2 2 3 4 4 1-1 1-1 2-1l2 1c1 1 2 2 1 3-2 2-5 1-8-2S0 3 2 1z" fill="var(--navy)"/></svg></span>
    <span>+1 (555) 014-2290</span>
  </div>
  <div class="contact" style="left:723px">
    <span class="contact__icon"><svg width="16" height="16" viewBox="0 0 16 16" fill="none" stroke="var(--navy)" stroke-width="1.4"><circle cx="8" cy="8" r="7"/><ellipse cx="8" cy="8" rx="3" ry="7"/><path d="M1 8h14"/></svg></span>
    <span>korvantech.com</span>
  </div>

  <div class="partner" style="left:61px;width:68px"></div>
  <div class="partner" style="left:150px;width:125px"></div>
  <div class="partner" style="left:296px;width:78px"></div>
  <div class="partner partner--dark" style="left:391px;width:136px"></div>
  <div class="partner" style="left:544px;width:166px"></div>
  <div class="partner" style="left:734px;width:152px"></div>
</main>
</body>
</html>
```